Poster design needed for Pregnant class 25.11.2018*

We need a poster design with the instruction details:
- Size: A4- Content:
1. Logo
2. Title of poster: Pregnant class - Eating healthy while pregnant
3. Promote when join in out class: 30% off delivery package
4. Singapore - 25.11.2018
5. Detail of contact: please visit https://www.harbourvalehospital.com.sg/And get information for this poster.

Pregnant

Medical And Science

Sans Serif

85cae6
33a6d7

• Picture mom and baby or pregnant

```html
<!DOCTYPE html>
<html lang="en">
<head>
<meta charset="utf-8">
<title>Pregnant Class – Eating Healthy While Pregnant</title>
<link rel="stylesheet" href="https://fonts.googleapis.com/css2?family=Raleway:wght@600;700;800&family=Roboto+Condensed:wght@700&family=Oswald:wght@600&family=Roboto:wght@400;500&family=Merriweather:wght@400&display=swap">
<style>
  :root {
    --sky: #85cae6;
    --ocean: #33a6d7;
    --frame: #5cbde6;
    --frame-deep: #4fb3df;
    --ink: #333333;
    --slate: #7b7b7b;
    --paper: #ffffff;
    --sand: #b2a87e;
    --line: #2b8fc4;
  }
  html, body {
    margin: 0;
    width: 1200px;
    height: 1200px;
    overflow: hidden;
    background: var(--paper);
  }
  .poster {
    position: absolute;
    left: 251px;
    top: 104px;
    width: 699px;
    height: 990px;
    background: linear-gradient(135deg, var(--sky) 0%, var(--frame) 45%, var(--frame-deep) 100%);
  }
  .content-card {
    position: absolute;
    left: 31px;
    top: 32px;
    width: 637px;
    height: 825px;
    background: var(--paper);
    border: 1px solid var(--line);
    border-radius: 26px;
    overflow: hidden;
  }
  .hero-art {
    position: absolute;
    z-index: 0;
    left: 18px;
    top: 136px;
    width: 305px;
    height: 690px;
    border-radius: 120px 120px 0 0;
    background: radial-gradient(ellipse at 55% 55%, #5cc4f0 0%, var(--ocean) 55%, #2f9fd3 100%);
    opacity: .92;
  }
  .headline {
    position: absolute;
    z-index: 1;
    right: 24px;
    margin: 0;
    text-align: right;
    white-space: nowrap;
  }
  .title-pregnant { top: 58px; font: 800 59px/1 "Raleway", sans-serif; color: var(--ocean); letter-spacing: 1px; }
  .title-class { top: 130px; font: 800 72px/1 "Raleway", sans-serif; color: var(--slate); }
  .topic { top: 256px; font: 700 38px/1.15 "Roboto Condensed", sans-serif; }
  .topic .accent { color: var(--ocean); display: block; }
  .topic .plain { color: var(--ink); display: block; }
  .promo-lead { top: 394px; font: 700 28px/1.22 "Raleway", sans-serif; }
  .promo-lead .accent { color: var(--ocean); display: block; }
  .promo-lead .plain { color: var(--ink); font-weight: 600; display: block; }
  .offer { top: 466px; font: 600 66px/1 "Oswald", sans-serif; color: var(--ocean); letter-spacing: -1px; }
  .offer-note { top: 538px; font: 500 23px/1 "Roboto", sans-serif; color: var(--ink); }
  .place { top: 620px; font: 500 33px/1 "Roboto", sans-serif; color: var(--ocean); }
  .date { top: 660px; font: 500 42px/1 "Roboto", sans-serif; color: var(--ink); }
  .more { top: 750px; font: 500 22px/1 "Roboto", sans-serif; color: var(--ocean); }
  .web {
    top: 784px;
    font: 400 16px/1 "Roboto", sans-serif;
    color: var(--ink);
    display: flex;
    align-items: center;
    gap: 8px;
  }
  .web .domain { color: var(--ocean); }
  .brand-bar {
    position: absolute;
    left: 31px;
    top: 880px;
    width: 637px;
    height: 87px;
    background: var(--paper);
    border: 1px solid var(--line);
    border-radius: 26px;
    overflow: hidden;
  }
  .brand-bar svg { position: absolute; left: 0; top: 0; }
  .brand-name {
    position: absolute;
    left: 132px;
    top: 40px;
    font: 400 20px/1 "Merriweather", serif;
    color: var(--paper);
  }
  .brand-tagline {
    position: absolute;
    left: 328px;
    top: 70px;
    font: 500 11px/1 "Roboto", sans-serif;
    letter-spacing: 3px;
    color: var(--sand);
  }
</style>
</head>
<body>
  <main class="poster">
    <section class="content-card">
      <div class="hero-art" role="img" aria-label="Blue watercolour silhouette of a pregnant woman in profile"></div>

      <h1 class="headline title-pregnant">PREGNANT</h1>
      <p class="headline title-class">CLASS</p>

      <h2 class="headline topic">
        <span class="accent">Eating Healthy</span>
        <span class="plain">While Pregnant</span>
      </h2>

      <p class="headline promo-lead">
        <span class="accent">Promote when</span>
        <span class="plain">join in out class:</span>
      </p>
      <p class="headline offer">30% OFF</p>
      <p class="headline offer-note">DELIVERY PACKAGE</p>

      <p class="headline place">SINGAPORE</p>
      <p class="headline date">25.11.2018</p>

      <p class="headline more">For More details Visit</p>
      <p class="headline web">
        <svg width="16" height="16" viewBox="0 0 16 16" aria-hidden="true">
          <circle cx="8" cy="8" r="6.5" fill="none" stroke="#33a6d7" stroke-width="1.4"/>
          <ellipse cx="8" cy="8" rx="3" ry="6.5" fill="none" stroke="#33a6d7" stroke-width="1.2"/>
          <line x1="1.5" y1="8" x2="14.5" y2="8" stroke="#33a6d7" stroke-width="1.2"/>
        </svg>
        <span>www.<span class="domain">harbourvalehospital</span>.com.sg</span>
      </p>
    </section>

    <footer class="brand-bar">
      <svg width="637" height="87" viewBox="0 0 637 87" aria-hidden="true">
        <polygon points="0,0 364,0 298,87 0,87" fill="#b2a87e"/>
      </svg>
      <span class="brand-name">Harbourvale</span>
      <span class="brand-tagline">CARE FOR LIFE.</span>
    </footer>
  </main>
</body>
</html>
```